Redesign of my business card

I would like to redesign my business card attached is my old version the new one. I’d like using my new logo that you designed that looks amazing thank you.

I would like the new card to be minimalist Brook Estate Group’s two key activities. I would also like on the card commercial cleaning at Facilities maintenance.

```html
<!DOCTYPE html>
<html lang="en">
<head>
<meta charset="utf-8">
<title>Brook Estate Group — Business Card</title>
<link href="https://fonts.googleapis.com/css2?family=Arimo:wght@400;700&display=swap" rel="stylesheet">
<style>
  :root {
    --brand-blue: #1570b9;
    --brand-blue-deep: #0f5fa3;
    --ink: #3c3c3c;
    --ink-soft: #6b6b6b;
    --paper: #ffffff;
    --stage: #e9ebee;
    --curve-dark: #2d2f33;
  }
  * { box-sizing: border-box; margin: 0; padding: 0; }
  html, body {
    width: 1200px; height: 874px; overflow: hidden;
    background: var(--stage);
    font-family: "Arimo", Arial, sans-serif;
  }
  .canvas {
    width: 1200px; height: 874px;
    display: flex; flex-direction: column; align-items: center; justify-content: center;
    gap: 40px;
  }
  .card {
    position: relative;
    width: 665px; height: 380px;
    border-radius: 22px;
    overflow: hidden;
    box-shadow: 0 6px 18px rgba(0,0,0,0.18);
  }
  /* Front */
  .card-front {
    background: var(--brand-blue);
    color: var(--paper);
  }
  .front-wordmark {
    position: absolute; left: 0; right: 0; top: 140px;
    text-align: center;
    font-weight: 700; font-size: 48px; letter-spacing: 0.5px;
    color: var(--paper);
  }
  .front-services {
    position: absolute; left: 0; right: 0; bottom: 62px;
    text-align: center;
    font-size: 19px; letter-spacing: 0.3px;
  }
  .front-services .sep { margin: 0 14px; }
  /* Back */
  .card-back { background: var(--paper); }
  .back-wave { position: absolute; left: 0; bottom: 0; width: 665px; height: 380px; }
  .back-wordmark {
    position: absolute; left: 40px; top: 118px; width: 250px;
    font-weight: 700; font-size: 26px; line-height: 1.15;
    color: var(--brand-blue);
  }
  .back-divider {
    position: absolute; left: 322px; top: 96px;
    width: 1px; height: 150px;
    background: linear-gradient(to bottom, rgba(0,0,0,0), #9a9a9a 30%, #9a9a9a 70%, rgba(0,0,0,0));
  }
  .contact-block { position: absolute; left: 346px; top: 104px; }
  .person-name {
    font-weight: 700; font-size: 30px; color: var(--brand-blue);
  }
  .person-role {
    font-size: 16px; color: var(--ink-soft); margin-top: 2px; margin-bottom: 16px;
  }
  .contact-list { list-style: none; }
  .contact-list li {
    display: flex; align-items: center; gap: 10px;
    font-size: 17px; color: var(--ink); line-height: 1.45;
  }
  .contact-list svg { width: 14px; height: 14px; fill: var(--brand-blue); flex: none; }
</style>
</head>
<body>
<main class="canvas">

  <section class="card card-front" aria-label="Card front">
    <div class="front-wordmark">Brook Estate Group</div>
    <p class="front-services">Commercial Cleaning<span class="sep">|</span>Facilities Maintenance</p>
  </section>

  <section class="card card-back" aria-label="Card back">
    <svg class="back-wave" viewBox="0 0 665 380" aria-hidden="true">
      <path d="M0 238 C 150 300, 380 345, 665 338 L665 380 L0 380 Z" fill="var(--brand-blue)"/>
      <path d="M0 226 C 150 292, 380 334, 665 334 L665 340 C 380 343, 150 302, 0 240 Z" fill="var(--curve-dark)"/>
    </svg>

    <div class="back-wordmark">Brook Estate Group</div>
    <div class="back-divider"></div>

    <div class="contact-block">
      <h1 class="person-name">Daniel Hartley</h1>
      <p class="person-role">President</p>
      <ul class="contact-list">
        <li>
          <svg viewBox="0 0 24 24"><path d="M6.6 10.8a15.1 15.1 0 0 0 6.6 6.6l2.2-2.2a1 1 0 0 1 1-.25 11.4 11.4 0 0 0 3.6.57 1 1 0 0 1 1 1V20a1 1 0 0 1-1 1A17 17 0 0 1 3 4a1 1 0 0 1 1-1h3.5a1 1 0 0 1 1 1c0 1.25.2 2.45.57 3.57a1 1 0 0 1-.25 1z"/></svg>
          0400 555 018
        </li>
        <li>
          <svg viewBox="0 0 24 24"><path d="M2 5h20v14H2z M2 5l10 8 10-8" fill="none" stroke="var(--brand-blue)" stroke-width="2"/></svg>
          info@brookestate.com.au
        </li>
        <li>
          <svg viewBox="0 0 24 24"><circle cx="12" cy="12" r="10"/></svg>
          www.brookestate.com.au
        </li>
      </ul>
    </div>
  </section>

</main>
</body>
</html>
```